KMW Plumbing and Roofing

design a fresh modern card for a young plumbing business looking to break into the market.
Must include the logo in the attached file
Bryce Olmo Verity
Phone number 0413962840
Vic Licence no 63194
email......

New Homes & Renovations
General Plumbing & Maintenance
Solar Hot Water Units
Roofing & Guttering (new and replacement)

Industry/Entity Type

Business

```html
<!DOCTYPE html>
<html lang="en">
<head>
<meta charset="utf-8">
<title>KMW Plumbing and Roofing – Business Card</title>
<link href="https://fonts.googleapis.com/css2?family=Open+Sans:wght@400;600;700&family=Exo+2:wght@600;700&family=Pinyon+Script&display=swap" rel="stylesheet">
<style>
  :root {
    --backdrop: #2b2b2b;
    --orange: #f05a28;
    --orange-bright: #f7701f;
    --navy: #073660;
    --white: #ffffff;
    --gold-light: #f6c453;
    --gold-dark: #c98a1a;
    --shadow: rgba(0,0,0,0.45);
  }
  * { margin: 0; padding: 0; box-sizing: border-box; }
  html, body { width: 1200px; height: 900px; overflow: hidden; }
  body { background: var(--backdrop); position: relative; font-family: "Open Sans", sans-serif; }

  .card {
    position: absolute;
    width: 582px;
    height: 350px;
    border-radius: 14px;
    overflow: hidden;
    box-shadow: 0 6px 18px var(--shadow);
  }

  /* Front */
  .card--front { left: 382px; top: 82px; background: var(--orange); color: var(--white); text-align: center; }
  .brand { position: absolute; display: flex; align-items: center; gap: 12px; }
  .brand__mark { width: 22px; height: 22px; border-radius: 50%; flex: none; }
  .brand__name { font-family: "Open Sans", sans-serif; font-weight: 700; font-size: 25px; white-space: nowrap; }
  .card--front .brand { left: 0; right: 0; top: 110px; justify-content: center; }
  .card--front .brand__mark { background: var(--white); }
  .card--front .brand__name { color: var(--white); }

  .services { position: absolute; left: 0; right: 0; top: 174px; list-style: none; font-size: 16.5px; line-height: 21.5px; }
  .tagline { position: absolute; left: 0; right: 0; top: 272px; font-family: "Pinyon Script", cursive; font-size: 22px; }

  /* Back */
  .card--back { left: 371px; top: 498px; background: var(--navy); }
  .card__shape { position: absolute; inset: 0; }
  .card--back .brand { left: 16px; top: 140px; width: 250px; }
  .card--back .brand__mark { background: var(--navy); }
  .card--back .brand__name { color: var(--navy); font-size: 22px; line-height: 28px; white-space: normal; max-width: 210px; }

  .contact-name {
    position: absolute; left: 314px; top: 38px;
    font-family: "Exo 2", sans-serif; font-weight: 700; font-size: 25px;
    background: linear-gradient(180deg, var(--gold-light), var(--gold-dark));
    -webkit-background-clip: text; background-clip: text; color: transparent;
  }
  .contact-phone { position: absolute; left: 322px; top: 80px; font-size: 19px; color: var(--white); }
  .label { color: var(--orange-bright); }
  .contact-details { position: absolute; left: 293px; top: 276px; font-size: 14.5px; line-height: 19.5px; color: var(--white); }
</style>
</head>
<body>

  <section class="card card--front">
    <div class="brand">
      <span class="brand__mark"></span>
      <span class="brand__name">KMW Plumbing and Roofing</span>
    </div>
    <ul class="services">
      <li>general plumbing and maintenance</li>
      <li>solar hot water units</li>
      <li>roofing and guttering (new and replacement)</li>
      <li>Septic tanks and much more</li>
    </ul>
    <p class="tagline">" Quality is the key"</p>
  </section>

  <section class="card card--back">
    <svg class="card__shape" width="582" height="350" viewBox="0 0 582 350" aria-hidden="true">
      <path d="M0,0 H272 C340,100 335,250 212,350 H0 Z" fill="var(--orange-bright)"/>
      <path d="M0,0 H265 C325,95 320,245 190,350 H0 Z" fill="var(--white)"/>
    </svg>
    <div class="brand">
      <span class="brand__mark"></span>
      <span class="brand__name">KMW Plumbing and Roofing</span>
    </div>
    <h1 class="contact-name">Bryce Olmo Verity</h1>
    <p class="contact-phone"><span class="label">Phone : </span>0413962840</p>
    <p class="contact-details">
      <span class="label">Vic Licence no : </span>63194<br>
      <span class="label">Email :</span><br>
      kmwplumbingandroofing@mailbox.com
    </p>
  </section>

</body>
</html>
```